Updated LURO Brochure for cultural event

We are seeking an updated brochure in a standard 8.5 by 11 size, and we have provided the current brochure and necessary information for inclusion. We desire a fresh new design that conveys a modern and elegant aesthetic. As we anticipate making changes to the brochure periodically, we require an editable program for its creation. Our First Nation Community values our beliefs and appearance, and we hope the brochure will reflect our welcoming nature while standing out from the crowd.
Attached Brochure is from last year
Wants and needs:
Page one. A redesign All the info on the page needs to be there but it needs a face lift.
Page two. Information is attached for that but do need this page editable for future. Join us for an immersive cultural experience at Pell Creek First Nation (PCFN) community, located in Northeastern BC. We invite you to participate in the Luro Camping Experience, a unique opportunity to forge relationships with our community, connect with our Chief and Council, and engage with industry leaders. Your participation in this grassroots event will earn your company credibility for the work it performs in PCFN territory.

Through this experience, you'll gain an appreciation and understanding of our community and cultural values, while meeting with key office staff, industry C-Suite level executives, industry Indigenous relations staff, and local, regional, and provincial representatives in a positive and welcoming space. The recent Marten V. British Columbia 2021 decision has significantly shifted how consultation and engagement will be managed on our lands. To help you better understand why managing cumulative effects is essential to PCFN, we welcome you to join us for a three-day camping experience from May 23 to May 26, 2023.

The Luro Camping Experience offers a variety of activities, including a dinner visit to NAH 'T'zo, the 12,500-year-old cave, where an archeological dig is currently underway, accompanied by our economic development corporation team from Ravik Development LP. The event also includes traditional bush camping in elegant teepees/wall tents, dry meat making, and participation in our Pell Day, a 30+ year cultural education and anti-racism event held on May 25, 2023. During Pell Day, over 400+ students from School District #47 participate in traditional activities, including moose hide preparation, beaver skinning, archaeology dig, dry-meat making, trapping demonstrations, Bannock on a stick, storytelling, drumming, and tea dance around the campfire to the beat of our drums.

Root yourself to the land, connect with your inner self, and be transformed alongside other important dignitaries as you partake in these multi-sensory experiences on our cultural grounds. This is our second combined camping/Pell Day experience, and we hope to continue and build on it for future cultural tourism activities such as guided bush camps, hikes, and hunts.

If you are unable to join us for the full three-day camping experience, we encourage you to join us for the one-day Pell Day event, along with other important decision-makers and political leaders. We have a helicopter landing area close to the activities for your convenience. Please RSVP to Owen Fisk, Neh? T'zo Cultural Productions Manager at OwenFisk@pellcreekfn-example.com or Brent Tally, PCFN Councilor at Btally@pellcreekfn-example.com. We are looking forward to hosting you!

Page 3 - Signatures Names can be put in but I will need to add signatures after.
Page 4. 2023 Sponsors this will need to be editable as we get new ones in.
Page 5. Participant supplies check list. All of this is good just need to make it look better
Page 6. Agenda Dates need to change May 23-26 2023 This page also needs to be editable .. the days Dates need to change also.
Page 7 . Same info can be there.
All pages can use different photos where you need them..
Different logos on the sponsor page so that needs to be editable.
Daily Agenda needs to be editable .. definitely a better table

Things that need to be editable are dates (May 23-26th 2023)

I am just gathering some more photos for the brochure and will add them as I go .

Target Market(s)

Corporate partners

Colors
0054AA
0677BA
7BADD7
CADEEF
E8F1F8
0094D4
00A9DD
6FCCEA
C7EBF8
E9F6FB
00AB8E
00BBA5
67D7C9
C6EFE9
E9F9F6
59FF00
82FF00
B8FF75
E3FFCB
F4FFEA
FFF300
FFF600
FEFA6F
FFFEC7
FFFEE8
FFC000
F8CF3A
FAE287
FDF2CF
FEFAEE
F0912C
F2A743
F7CA91
FBE8D2
FDF5EE
EE7325
F08F49
F5BC92
FAE3D3
FDF4ED
EB3D1F
EC4F4E
F09395
F8D3D4
FCEDEE

Requirements
Must have
• The information that was provided
Nice to have
• We would like this to be very inviting and professional
Should not have
• cartoons or anything that looks cheap

```html
<!DOCTYPE html>
<html lang="en">
<head>
<meta charset="utf-8">
<title>Luro Executive Camping Experience – Brochure</title>
<link href="https://fonts.googleapis.com/css2?family=Cinzel:wght@400;600&family=Montserrat:wght@400;500;600;700&family=Oswald:wght@500&display=swap" rel="stylesheet">
<style>
:root{
  --stage:#e9e9ea;
  --paper:#f7f5f1;
  --paper-warm:#ece6dc;
  --sponsor-grey:#d9d6d2;
  --ink:#2b2b2b;
  --ink-soft:#6a6a6a;
  --rule:#c9c6c1;
  --night:#1b2233;
  --night-deep:#121620;
  --accent-green:#00AB8E;
  --accent-red:#EB3D1F;
  --white:#ffffff;
}
*{box-sizing:border-box;margin:0;padding:0}
html,body{width:1200px;height:2243px;overflow:hidden;background:var(--stage)}
body{position:relative;font-family:"Montserrat",Arial,sans-serif;color:var(--ink)}
.page{position:absolute;overflow:hidden;background:var(--paper);box-shadow:0 6px 18px rgba(0,0,0,.12)}
.photo{position:absolute}

/* Brand name set as plain text */
.brand-name{font-family:"Montserrat",Arial,sans-serif;font-weight:500;color:var(--white);letter-spacing:2px}

/* ROW 1 */
.cover{left:70px;top:170px;width:340px;height:440px;background:var(--night)}
.cover .photo{inset:0;background:linear-gradient(170deg,#1d2a4a 0%,#2c3550 40%,#4a3a2a 75%,#1a1712 100%)}
.cover .brand-name{position:absolute;right:26px;top:46px;font-size:16px}
.cover .title{position:absolute;left:0;right:0;top:150px;text-align:center;color:var(--white);font-family:"Cinzel",Georgia,serif}
.cover .title .t1{font-size:10px;letter-spacing:3px}
.cover .title .t2{font-size:9px;letter-spacing:4px;margin-top:6px;opacity:.9}
.cover .nation{position:absolute;left:22px;bottom:22px;color:var(--white);font-size:8px;font-weight:600;letter-spacing:1px}

.intro{left:430px;top:170px;width:340px;height:440px;background:var(--paper-warm)}
.intro .photo{left:0;top:0;width:340px;height:110px;background:linear-gradient(180deg,#8fa3a6,#6b7d62)}
.intro .body{position:absolute;left:30px;right:26px;top:128px;font-size:5.6px;line-height:1.55;color:#444}
.intro .body p{margin-bottom:5px}
.intro .body .close{font-weight:700;color:var(--ink)}

.signatures{left:790px;top:170px;width:340px;height:440px;background:var(--white)}
.signatures h2{position:absolute;left:30px;top:34px;font-family:"Cinzel",Georgia,serif;font-size:10px;letter-spacing:3px;font-weight:400}
.sig-grid{position:absolute;left:30px;right:30px;top:60px;display:grid;grid-template-columns:1fr 1fr;row-gap:20px;column-gap:24px}
.sig .line{height:20px;border-bottom:1px solid var(--rule)}
.sig .who{font-size:7px;font-weight:600;letter-spacing:1px;margin-top:4px}
.sig .role{font-size:6px;color:var(--ink-soft)}
.signatures .photo{left:0;bottom:0;width:340px;height:150px;background:linear-gradient(180deg,#f2f1ee,#d8d2c8)}

/* ROW 2 */
.sponsors{left:230px;top:880px;width:370px;height:480px;background:var(--sponsor-grey)}
.sponsors .photo{left:0;top:0;width:370px;height:150px;background:linear-gradient(180deg,#aab6b8 0%,#8b9aa0 45%,#7d9a4e 80%,#c4b13c 100%)}
.sponsors h2{position:absolute;left:0;right:0;top:14px;text-align:center;font-family:"Oswald",Arial,sans-serif;font-weight:500;font-size:32px;letter-spacing:9px;color:var(--white)}
.sponsor-grid{position:absolute;left:22px;right:22px;top:176px;display:grid;grid-template-columns:repeat(4,1fr);column-gap:12px;row-gap:44px}
.sponsor{height:28px;background:var(--white);display:flex;align-items:center;justify-content:center;gap:4px;font-size:6.5px;font-weight:600;color:#3a4654;text-align:center;line-height:1.1;padding:0 3px}
.sponsor .dot{width:7px;height:7px;border-radius:50%;background:#3a4654;flex:none}

.checklist{left:600px;top:880px;width:370px;height:480px;background:#8a7b6a}
.checklist .photo{inset:0;background:linear-gradient(90deg,#7d6f60,#9a8b7a 50%,#7a6c5d)}
.sheet{position:absolute;left:44px;top:70px;width:290px;height:350px;background:var(--white);padding:16px 14px;box-shadow:0 2px 6px rgba(0,0,0,.25)}
.sheet h2{font-family:"Cinzel",Georgia,serif;font-weight:400;font-size:8.5px;letter-spacing:2px;text-align:center}
.sheet .lede{font-size:4.6px;color:var(--ink-soft);text-align:center;line-height:1.5;margin-top:5px}
.sheet .temp{font-size:5px;font-weight:700;text-align:center;margin:4px 0 6px}
.chk{width:100%;border-collapse:collapse;font-size:4.6px}
.chk th,.chk td{border:0.5px solid var(--rule);padding:1.2px 2px;text-align:left;height:7.5px}
.chk th{font-family:"Cinzel",Georgia,serif;font-size:4.2px;background:#f1f1f1}
.chk th.have{color:var(--accent-green)}
.chk th.need{color:var(--accent-red)}
.chk .note{color:var(--ink-soft);font-size:4px}
.chk .group th{text-align:center;background:var(--white);border-left:0;border-right:0;padding-top:6px}
.sheet .foot{font-size:4.4px;color:var(--ink-soft);text-align:right;margin-top:6px;line-height:1.5}
.sheet .foot b{color:var(--ink)}

/* ROW 3 */
.agenda{left:230px;top:1640px;width:370px;height:480px;background:var(--paper-warm)}
.agenda h2{position:absolute;left:32px;top:30px;font-family:"Cinzel",Georgia,serif;font-weight:400;font-size:8px;letter-spacing:2.5px}
.plan{position:absolute;left:32px;top:48px;width:312px;border-collapse:collapse;font-size:4.4px;table-layout:fixed}
.plan th,.plan td{border:0.5px solid var(--rule);padding:0.8px 2px;height:7.4px;text-align:left;vertical-align:middle}
.plan th{font-weight:500;color:var(--ink-soft)}
.plan .c-day{width:42px}
.plan .c-time{width:32px}
.plan .c-note{width:66px}
.plan .day{text-align:center;font-weight:700}
.plan .time{white-space:nowrap}
.plan .all td{background:#dedad3;font-weight:700}
.plan .note{color:var(--ink-soft);font-size:3.8px}
.agenda .photo{left:0;bottom:0;width:370px;height:140px;background:linear-gradient(180deg,#e8c3a6 0%,#9aa6a8 40%,#5c6a5a 100%)}

.closing{left:600px;top:1640px;width:370px;height:480px;background:var(--night-deep)}
.closing .photo{inset:0;background:radial-gradient(circle at 50% 78%,#b55a1c 0%,#4a2a14 18%,#1b1c26 45%,#15161d 100%)}
.closing .brand-name{position:absolute;left:0;right:0;top:120px;text-align:center;font-size:16px}
.closing .message{position:absolute;left:0;right:0;top:340px;text-align:center;color:var(--white)}
.closing .message .m1{font-family:"Cinzel",Georgia,serif;font-size:9px;letter-spacing:3px;line-height:1.5}
.closing .message .m2{font-size:10px;margin-top:18px}
.closing .message .m3{font-family:"Cinzel",Georgia,serif;font-size:8.5px;letter-spacing:3px;margin-top:22px}
</style>
</head>
<body>

<section class="page cover">
  <div class="photo" role="img" aria-label="Night sky with milky way over a lit camp of tents and people by a campfire"></div>
  <div class="brand-name">Luro Experiences</div>
  <div class="title">
    <div class="t1">LURO EXECUTIVE CAMPING EXPERIENCE</div>
    <div class="t2">PELL DAY 2023</div>
  </div>
  <div class="nation">Pell Creek First Nation</div>
</section>

<section class="page intro">
  <div class="photo" role="img" aria-label="Hiker standing on a mountain trail above a green valley"></div>
  <div class="body">
    <p>Join us for an immersive cultural experience at Pell Creek First Nation (PCFN) community, located in Northeastern BC. We invite you to participate in the Luro Camping Experience, a unique opportunity to forge relationships with our community, connect with our Chief and Council, and engage with industry leaders. Your participation in this grassroots event will earn your company credibility for the work it performs in PCFN territory.</p>
    <p>Through this experience, you'll gain an appreciation and understanding of our community and cultural values, while meeting with key office staff, industry C-Suite level executives, industry Indigenous relations staff, and local, regional, and provincial representatives in a positive and welcoming space. The recent Marten V. British Columbia 2021 decision has significantly shifted how consultation and engagement will be managed on our lands. To help you better understand why managing cumulative effects is essential to PCFN, we welcome you to join us for a three-day camping experience from May 23 to May 26, 2023.</p>
    <p>The Luro Camping Experience offers a variety of activities, including a dinner visit to NAH 'T'zo, the 12,500-year-old cave, where an archeological dig is currently underway, accompanied by our economic development corporation team from Ravik Development LP. The event also includes traditional bush camping in elegant teepees/wall tents, dry meat making, and participation in our Pell Day, a 30+ year cultural education and anti-racism event held on May 25, 2023. During Pell Day, over 400+ students from School District #47 participate in traditional activities, including moose hide preparation, beaver skinning, archaeology dig, dry-meat making, trapping demonstrations, Bannock on a stick, storytelling, drumming, and tea dance around the campfire to the beat of our drums.</p>
    <p>Root yourself to the land, connect with your inner self, and be transformed alongside other important dignitaries as you partake in these multi-sensory experiences on our cultural grounds. This is our second combined camping/Pell Day experience, and we hope to continue and build on it for future cultural tourism activities such as guided bush camps, hikes, and hunts.</p>
    <p>If you are unable to join us for the full three-day camping experience, we encourage you to join us for the one-day Pell Day event, along with other important decision-makers and political leaders. We have a helicopter landing area close to the activities for your convenience. Please RSVP to Owen Fisk, Neh? T'zo Cultural Productions Manager at OwenFisk@pellcreekfn-example.com or Brent Tally, PCFN Councilor at Btally@pellcreekfn-example.com.</p>
    <p class="close">We are looking forward to hosting you!</p>
  </div>
</section>

<section class="page signatures">
  <h2>SIGNATURES</h2>
  <div class="sig-grid">
    <div class="sig"><div class="line"></div><div class="who">DALE KORWIN</div><div class="role">Chief PCFN</div></div>
    <div class="sig"><div class="line"></div><div class="who">NAME GOES HERE</div><div class="role">Position Goes Here</div></div>
    <div class="sig"><div class="line"></div><div class="who">BRENT TALLY</div><div class="role">PCFN Councillor</div></div>
    <div class="sig"><div class="line"></div><div class="who">NAME GOES HERE</div><div class="role">Position Goes Here</div></div>
    <div class="sig"><div class="line"></div><div class="who">TESSA HOLLOWAY</div><div class="role">PCFN Councillor</div></div>
    <div class="sig"></div>
    <div class="sig"><div class="line"></div><div class="who">MIRA SAND</div><div class="role">PCFN Councillor</div></div>
  </div>
  <div class="photo" role="img" aria-label="Flat lay of camping gear: knives, hat, shovel, canvas bag and lantern"></div>
</section>

<section class="page sponsors">
  <div class="photo" role="img" aria-label="Camper resting on a sleeping pad beside an orange tent in an alpine meadow"></div>
  <h2>2023 SPONSORS</h2>
  <div class="sponsor-grid">
    <div class="sponsor"><span class="dot"></span>Northvale Energy</div>
    <div class="sponsor">Larch Energy</div>
    <div class="sponsor">Ridge Nine</div>
    <div class="sponsor">Basin Resource Office</div>
    <div class="sponsor">Bluestone</div>
    <div class="sponsor">Kestrel Well</div>
    <div class="sponsor">Quartzline Resources</div>
    <div class="sponsor">Aurel</div>
    <div class="sponsor">Fenmark</div>
    <div class="sponsor">Summit Safety</div>
    <div class="sponsor">Graniteway</div>
    <div class="sponsor">Ravik Contracting</div>
    <div class="sponsor">Tamlin Exploration</div>
    <div class="sponsor">Sedgewell</div>
    <div class="sponsor">Luro Experiences</div>
    <div class="sponsor">Pell Creek First Nation</div>
  </div>
</section>

<section class="page checklist">
  <div class="photo" role="img" aria-label="Weathered wooden planks with rope, binoculars, headlamp, hiking boots and a compass"></div>
  <div class="sheet">
    <h2>PARTICIPANT SUPPLIES CHECKLIST</h2>
    <p class="lede">We will be outside regardless of the weather so dress accordingly. If you do not have gear or clothes from this checklist please let us know and we will outfit you to ensure you are comfortable and warm. You will be cuddled by the fire at night.</p>
    <p class="temp">Average local temp for May is + 16 to + 4</p>
    <table class="chk">
      <tr><th>ITEM</th><th class="have">HAVE</th><th class="need">NEED</th><th>NOTES</th></tr>
      <tr><td>Pillow</td><td></td><td></td><td></td></tr>
      <tr><td>Personal medication</td><td></td><td></td><td></td></tr>
      <tr><td>Allergy medication (if applicable)</td><td></td><td></td><td></td></tr>
      <tr><td>Own tent if preferred or you snore obnoxiously</td><td></td><td></td><td></td></tr>
      <tr><td>Warm weather top</td><td></td><td></td><td></td></tr>
      <tr><td>Spring weather jacket</td><td></td><td></td><td></td></tr>
      <tr><td>Spring weather base layers</td><td></td><td></td><td></td></tr>
      <tr><td>Rain shell (check weather)</td><td></td><td></td><td></td></tr>
      <tr><td>Hat &amp; mitts/gloves</td><td></td><td></td><td></td></tr>
      <tr><td>Sunscreen</td><td></td><td></td><td></td></tr>
      <tr><td>Pocket knife (checked luggage)</td><td></td><td></td><td></td></tr>
      <tr><td>4 pairs wool or polyester socks</td><td></td><td></td><td></td></tr>
      <tr><td>Camp shoes</td><td></td><td></td><td></td></tr>
      <tr><td>Light hiking shoes/ rubber boots</td><td></td><td></td><td class="note">Mountain boots not required this experience</td></tr>
      <tr><td>Flashlight</td><td></td><td></td><td></td></tr>
      <tr><td>Water bottle</td><td></td><td></td><td></td></tr>
      <tr><td>Coffee Cup</td><td></td><td></td><td class="note">Not required but preferred</td></tr>
      <tr class="group"><th colspan="4">PELL CREEK SUPPLIED</th></tr>
      <tr><td>Tipi/wall tent for sleeping</td><td></td><td></td><td class="note">Wood stove provided for some tents</td></tr>
      <tr><td>Cot</td><td></td><td></td><td></td></tr>
      <tr><td>Insulated sleeping pad</td><td></td><td></td><td></td></tr>
      <tr class="group"><th colspan="4">NORTHVALE ENERGY SUPPLIED</th></tr>
      <tr><td>Sleeping bags</td><td></td><td></td><td class="note">Please let us know if you are a larger person</td></tr>
    </table>
    <p class="foot">Print this out and do your own gear bag checklist. No always begin on the more prepared.<br><b>This is not a comprehensive list.</b><br>Please contact Owen Fisk if you need assistance at anytime.<br>Email or text, then call<br><b>OwenFisk@pellcreekfn-example.com 250-555-0148</b></p>
  </div>
</section>

<section class="page agenda">
  <h2>PELL CREEK LURO EXECUTIVE EXPERIENCE</h2>
  <table class="plan">
    <colgroup><col class="c-day"><col class="c-time"><col><col class="c-note"></colgroup>
    <tr><th>DAY</th><th>TIME</th><th>ACTIVITY</th><th>DETAILS / NOTES</th></tr>
    <tr><td class="day" rowspan="6">Tuesday<br>May 23</td><td class="time">3:35 p.m.</td><td>Flight arrives from Calgary</td><td class="note"></td></tr>
    <tr><td class="time">4:00 p.m.</td><td>Depart for Nah 'T'zo</td><td class="note"></td></tr>
    <tr><td class="time">5:00 p.m.</td><td>Complete Nah 'T'zo tour</td><td class="note">Minivan from hotel, snacks</td></tr>
    <tr><td class="time">6:00 p.m.</td><td>Dinner with Glen Arbury &amp; Colin Mace, Ravik Dev.</td><td class="note">Return to hotel after dinner</td></tr>
    <tr><td class="time"></td><td>Overnight in FSJ one night</td><td class="note"></td></tr>
    <tr><td class="time"></td><td></td><td class="note"></td></tr>
    <tr><td class="day" rowspan="12">Wednesday<br>May 24</td><td class="time">7:30 a.m.</td><td>Pick up at hotel</td><td class="note"></td></tr>
    <tr><td class="time">8:00 a.m.</td><td>Depart hotel for Pell Creek</td><td class="note"></td></tr>
    <tr><td class="time">9:00 a.m.</td><td>Site visit to abandoned well</td><td class="note"></td></tr>
    <tr><td class="time">10:00 a.m.</td><td>Arrive PCFN &amp; start camp setup</td><td class="note"></td></tr>
    <tr><td class="time">11:00 a.m.</td><td>Gather in gym with Lands Office</td><td class="note">Discuss pending projects</td></tr>
    <tr><td class="time">12:00 p.m.</td><td>Lunch with Council</td><td class="note">Discuss valley plan</td></tr>
    <tr><td class="time">1:00 p.m.</td><td>Help prepare for Pell Days, set up their camp</td><td class="note"></td></tr>
    <tr><td class="time">2:00 p.m.</td><td>Board bus for community tour with Ray Arbury</td><td class="note"></td></tr>
    <tr><td class="time">4:00 p.m.</td><td>Return to camp - relax</td><td class="note"></td></tr>
    <tr class="all"><td class="time">ALL DAY</td><td>Drymeat making, bushcrafting, cooking camp</td><td class="note"></td></tr>
    <tr><td class="time">6:00 p.m.</td><td>Supper</td><td class="note"></td></tr>
    <tr><td class="time">8:00 p.m.</td><td>Campfire &amp; story telling or brush art collection</td><td class="note"></td></tr>
    <tr><td class="day" rowspan="7">Thursday<br>May 25</td><td class="time">6:30 a.m.</td><td>Breakfast at camp</td><td class="note"></td></tr>
    <tr><td class="time">10:00 a.m.</td><td>Pell Day starts</td><td class="note"></td></tr>
    <tr><td class="time">2:00 p.m.</td><td>Pell Day ends &amp; gather at camp to discuss learnings</td><td class="note"></td></tr>
    <tr class="all"><td class="time">ALL DAY</td><td>Drymeat making</td><td class="note"></td></tr>
    <tr><td class="time">6:00 p.m.</td><td>Supper at camp</td><td class="note"></td></tr>
    <tr><td class="time">7:00 p.m.</td><td>Hike/herb collection, make tea at camp</td><td class="note"></td></tr>
    <tr><td class="time">8:30 p.m.</td><td>More tea &amp; story telling</td><td class="note"></td></tr>
    <tr><td class="day" rowspan="6">Friday<br>May 26</td><td class="time">6:30 a.m.</td><td>Breakfast at camp</td><td class="note"></td></tr>
    <tr><td class="time">7:30 a.m.</td><td>Pack personal things</td><td class="note"></td></tr>
    <tr><td class="time">8:00 a.m.</td><td>Get on the bus</td><td class="note"></td></tr>
    <tr><td class="time">8:30 a.m.</td><td>Depart Pell for Airport</td><td class="note"></td></tr>
    <tr><td class="time">9:40 a.m.</td><td>Check in</td><td class="note"></td></tr>
    <tr><td class="time">11:05 a.m.</td><td>Flight departs</td><td class="note">Skyline Air SA3130</td></tr>
  </table>
  <div class="photo" role="img" aria-label="Hiker with a backpack overlooking mountain peaks above a sea of clouds at sunrise"></div>
</section>

<section class="page closing">
  <div class="photo" role="img" aria-label="People gathered around a campfire under a starry sky framed by autumn trees"></div>
  <div class="brand-name">Luro Experiences</div>
  <div class="message">
    <div class="m1">WE CAN'T WAIT TO<br>SEE YOU THERE</div>
    <div class="m2">Wuujǫ aasanaláá</div>
    <div class="m3">THANK YOU!</div>
  </div>
</section>

</body>
</html>
```